WAYmaker website redesign to provide information about experiential workshops, film work and other

We need a redesign of our website waymakerhub.org. We conduct experiential workshops of discovery and transformation for individuals and organizations. We need the website to reflect the full extent of WAYmaker programs, and be an information hub for WAYmaker workshops and communities as they develop.

The attached documents contain information about the organization - it's brandbook, copy for web pages, a website layout and a couple of images.

The site is for individuals and companies looking to promote and be change to make a difference. It should be warm, welcoming, and create excitement around the concepts and the ability to discover a new way of being in the world. We are about creating communities around the globe who will embody play, freedom, curiosity and expanded possibilities. We are creating a space for this to happen, both physically (workshops) and online.

We will be on either a SquareSpace, but mos tlikely a Weebly plaform.

Please look at the current site at www.waymakerhub.org

Target Market(s)

Initially, are target market will be baby boomers, but will expand to include millennials and students.

Coding

Coded - Design and coding required

Number of Pages Required

5+ page

Requirements
Must have
• The colors, logo and fonts from the brand book.
Nice to have
• Complimentary use of brand colors to create an attractive presentation and energy

```html
<!DOCTYPE html>
<html lang="en">
<head>
<meta charset="utf-8">
<title>WAYmaker — Experiential Workshops</title>
<link href="https://fonts.googleapis.com/css2?family=Montserrat:wght@500;700;800;900&family=Open+Sans:wght@400;600;700&display=swap" rel="stylesheet">
<style>
:root{
  --ink:#1b1b1b;
  --white:#ffffff;
  --paper:#f3f1f1;
  --orange:#f0a23e;
  --flame:#ef6a33;
  --green:#6dbd7c;
  --pink:#f6b3aa;
  --sky:#a7d7db;
  --dark:#222222;
  --grey-text:#333333;
  --line:#d9d9d9;
  --social:#2b4a8a;
}
*{box-sizing:border-box;margin:0;padding:0}
html,body{width:1200px;height:5158px;overflow:hidden}
body{font-family:"Open Sans",Arial,sans-serif;color:var(--ink);background:var(--white);position:relative}
.head{font-family:"Montserrat",Arial,sans-serif;font-weight:800;text-transform:uppercase}
section,header,footer{position:absolute;left:0;width:1200px;overflow:hidden}
.abs{position:absolute}

/* header */
.site-header{top:0;height:92px;background:var(--white)}
.brand{left:112px;top:28px;font-family:"Montserrat",sans-serif;font-weight:900;font-size:28px;letter-spacing:.5px;color:var(--ink);display:flex;align-items:center;gap:10px}
.brand-square{width:20px;height:20px;background:var(--ink)}
.main-nav{right:84px;top:44px;display:flex;gap:22px;font-family:"Montserrat",sans-serif;font-weight:700;font-size:11px;color:var(--ink)}

/* hero */
.hero{top:92px;height:630px}
.hero-photo{inset:0;background:linear-gradient(100deg,#6f7478 0%,#8d9296 45%,#a3a6a8 70%,#868a8d 100%)}
.hero-title{left:158px;top:132px;color:var(--white);font-size:37px;line-height:45px;letter-spacing:.5px}
.hero-title p+p{margin-top:28px}
.btn{display:flex;align-items:center;gap:12px;font-family:"Montserrat",sans-serif;font-weight:800;font-size:14px;text-transform:uppercase;color:var(--ink);padding:0 22px}
.btn-email{left:160px;top:390px;width:220px;height:44px;background:var(--orange)}
.btn-member{left:160px;top:454px;width:220px;height:46px;background:var(--pink)}

/* discover */
.discover{top:722px;height:1008px;background:var(--white)}
.discover-title{top:68px;left:0;width:1200px;text-align:center;font-size:22px;line-height:34px}
.tile{overflow:hidden}
.tile-photo{position:absolute}
.tile-label{position:absolute;font-family:"Montserrat",sans-serif;font-weight:800;text-transform:uppercase;color:var(--white);font-size:21px;line-height:23px;padding:24px 18px}
.t1{left:130px;top:200px;width:304px;height:378px}
.t2{left:450px;top:200px;width:302px;height:378px}
.t3{left:766px;top:200px;width:302px;height:378px}
.t4{left:130px;top:602px;width:460px;height:303px}
.t5{left:608px;top:602px;width:460px;height:303px}

/* vision */
.vision{top:1730px;height:558px;background:var(--paper)}
.vision-photo{left:612px;top:0;width:588px;height:558px;background:linear-gradient(160deg,#c9b78e 0%,#d8c79b 40%,#b39c6f 100%)}
.vision-title{left:130px;top:110px;font-size:44px}
.body-text{font-size:13.5px;line-height:21px;color:var(--grey-text)}
.body-text b{color:var(--ink)}
.vision-body{left:130px;top:188px;width:400px}
.vision-body p+p{margin-top:20px}

/* what we do */
.what{top:2288px;height:567px;background:var(--white)}
.what-photo{left:0;top:0;width:612px;height:567px;background:linear-gradient(135deg,#e8884a 0%,#d9663a 55%,#c8562f 100%)}
.what-title{left:698px;top:140px;font-size:44px}
.what-sub{left:698px;top:252px;font-size:17px;font-weight:800}
.what-body{left:698px;top:290px;width:400px}

/* movements */
.movements{top:2855px;height:455px;background:var(--orange)}
.movements-title{top:98px;left:0;width:1200px;text-align:center;font-size:22px;line-height:36px}
.move{top:220px;width:180px;text-align:center}
.move svg{display:block;margin:0 auto}
.move-label{margin-top:22px;font-family:"Montserrat",sans-serif;font-weight:800;font-size:13px;color:var(--ink)}

/* stirring the still */
.stir{top:3310px;height:842px;background:var(--paper)}
.stir-title{top:92px;left:0;width:1200px;text-align:center;font-size:30px}
.stir-rule{left:570px;top:150px;width:60px;height:4px;background:var(--orange)}
.stir-photo{left:516px;top:250px;width:684px;height:500px;background:linear-gradient(140deg,#9fcb8b 0%,#7fb470 50%,#5f9a57 100%)}
.stir-card{left:137px;top:309px;width:470px;height:390px;background:var(--white);padding:40px 36px 0 24px}
.stir-card p+p{margin-top:20px}
.stir-card .body-text{font-size:13px;line-height:20px}

/* community */
.community{top:4152px;height:636px;background:var(--dark)}
.community-bg{inset:0;background:radial-gradient(ellipse at 50% 40%,#3a3a3a 0%,#262626 60%,#1a1a1a 100%)}
.community-title{top:112px;left:0;width:1200px;text-align:center;font-size:32px;color:var(--white)}
.community-intro{top:168px;left:390px;width:420px;text-align:center;color:#dddddd;font-size:16px;line-height:23px}
.field{border:1.5px solid #cfcfcf;color:#e0e0e0;font-size:12px;padding:10px 12px;border-radius:3px}
.f-name{left:260px;top:292px;width:200px;height:38px}
.f-mail{left:480px;top:292px;width:200px;height:38px}
.f-phone{left:700px;top:292px;width:206px;height:38px}
.f-msg{left:260px;top:348px;width:646px;height:96px}
.submit{left:518px;top:498px;width:164px;height:38px;background:var(--orange);font-family:"Montserrat",sans-serif;font-weight:800;font-size:15px;display:flex;align-items:center;justify-content:center;color:var(--ink)}

/* footer */
.site-footer{top:4788px;height:370px;background:var(--white)}
.footer-brand{left:130px;top:136px;font-family:"Montserrat",sans-serif;font-weight:900;font-size:30px;letter-spacing:.5px;display:flex;align-items:center;gap:10px}
.col-title{font-family:"Montserrat",sans-serif;font-weight:800;font-size:12px}
.col{top:70px;font-size:12px;line-height:20px;color:var(--grey-text)}
.col-contact{left:515px}
.col-menu{left:750px}
.col-connect{left:940px}
.contact-row{display:flex;align-items:center;gap:12px;margin-top:16px}
.menu-list{margin-top:14px;list-style:none}
.social-row{display:flex;align-items:center;gap:10px;margin-top:14px}
.social-dot{width:22px;height:22px;border-radius:50%;background:var(--social)}
.footer-rule{left:130px;top:290px;width:940px;height:1px;background:var(--line)}
.copyright{top:318px;left:0;width:1200px;text-align:center;font-size:11px;color:var(--grey-text)}
</style>
</head>
<body>

<header class="site-header">
  <div class="abs brand"><span class="brand-square"></span>WAYmaker</div>
  <nav class="abs main-nav">
    <span>ABOUT US</span><span>WORKSHOPS</span><span>WAYMAKER PROJECTS</span><span>FILMS</span><span>STORE &amp; RESOURCES</span><span>COMMUNITY</span><span>CONTACT</span>
  </nav>
</header>

<section class="hero">
  <div class="abs hero-photo" role="img" aria-label="Woman seated on a chair beneath a chalk-drawn lightbulb full of ideas"></div>
  <div class="abs hero-title head">
    <p>What world do<br>we want to live in?</p>
    <p>What kind of life do<br>you want to create?</p>
  </div>
  <div class="abs btn btn-email">
    <svg width="16" height="12" viewBox="0 0 16 12"><rect x="0.5" y="0.5" width="15" height="11" fill="var(--ink)"/><path d="M1 1l7 6 7-6" stroke="var(--orange)" stroke-width="1.4" fill="none"/></svg>
    Email Capture
  </div>
  <div class="abs btn btn-member">
    <svg width="14" height="14" viewBox="0 0 14 14"><circle cx="7" cy="4" r="3.2" fill="var(--ink)"/><path d="M1 14c0-4 3-6 6-6s6 2 6 6z" fill="var(--ink)"/></svg>
    Member Login
  </div>
</section>

<section class="discover">
  <h2 class="abs discover-title head">Discover an opportunity to live a<br>more dynamic and meaningful life</h2>

  <div class="abs tile t1">
    <div class="tile-photo" style="left:0;top:0;width:304px;height:240px;background:linear-gradient(160deg,#5d7774,#2f4644)" role="img" aria-label="Dancers in bright costumes performing outdoors"></div>
    <div class="tile-label" style="left:0;top:240px;width:304px;height:138px;background:var(--flame);padding-top:44px">Moves<br>energy</div>
  </div>
  <div class="abs tile t2">
    <div class="tile-photo" style="left:0;top:0;width:302px;height:250px;background:linear-gradient(160deg,#5a4a52,#2d2a33)" role="img" aria-label="Group of people gathered in a workshop room"></div>
    <div class="tile-label" style="left:0;top:250px;width:302px;height:128px;background:var(--green);padding-top:22px">Creates<br>opportunities<br>for connecting</div>
  </div>
  <div class="abs tile t3">
    <div class="tile-photo" style="left:0;top:0;width:302px;height:250px;background:linear-gradient(160deg,#8f8a86,#4e4a48)" role="img" aria-label="Hands joined together in a circle"></div>
    <div class="tile-label" style="left:0;top:250px;width:302px;height:128px;background:var(--pink);padding-top:22px">Provides<br>opportunities<br>for collaboration<br>and creation</div>
  </div>
  <div class="abs tile t4">
    <div class="tile-photo" style="left:0;top:0;width:248px;height:303px;background:linear-gradient(160deg,#5a7a90,#1f2e3a)" role="img" aria-label="Silhouette of a man looking out over a city"></div>
    <div class="tile-label" style="left:248px;top:0;width:212px;height:303px;background:var(--sky);padding-top:92px">Deepens<br>experience<br>of life</div>
  </div>
  <div class="abs tile t5">
    <div class="tile-label" style="left:0;top:0;width:230px;height:303px;background:var(--ink);padding-top:92px">Supports<br>conscious<br>evolution</div>
    <div class="tile-photo" style="left:230px;top:0;width:230px;height:303px;background:linear-gradient(160deg,#7a6a5c,#3c332c)" role="img" aria-label="Participants seated in a circle on the floor"></div>
  </div>
</section>

<section class="vision">
  <h2 class="abs vision-title head">Vision</h2>
  <div class="abs vision-body body-text">
    <p><b>We envision a world</b> in which all people and communities can challenge and <b>break free</b> from stories that no longer serve us. We believe that solutions to contemporary challenges will emerge from a place of curiosity, love and connection.</p>
    <p>Through inspiration, <b>conscious reflection</b>, and collaboration, we <b>take responsibility</b> for the world <b>we are manifesting</b>, and we can discover and create new possibilities for the lives and the society we desire to build.</p>
  </div>
  <div class="abs vision-photo" role="img" aria-label="Man in a suit drawing a colourful lightbulb on a wall"></div>
</section>

<section class="what">
  <div class="abs what-photo" role="img" aria-label="Audience seated at a workshop, tinted orange"></div>
  <h2 class="abs what-title head">What we do</h2>
  <h3 class="abs what-sub head">WAYmaker Life</h3>
  <p class="abs what-body body-text">WAYmaker Life is a workshop designed to re-engage you with life. Through interactive exercises and personal exploration, you are taken on a journey that ultimately leaves you experiencing life as a Creator. You will learn to see beliefs and patterns that hold you back in work and relationships as well as a path to transforming the story of your life.</p>
</section>

<section class="movements">
  <h2 class="abs movements-title head">WAYmaker Life is a 2–3 day workshop<br>experienced in 5 movements</h2>
  <div class="abs move" style="left:82px">
    <svg width="84" height="84" viewBox="0 0 84 84"><circle cx="42" cy="42" r="30" fill="none" stroke="var(--ink)" stroke-width="3"/></svg>
    <div class="move-label">Curiosity</div>
  </div>
  <div class="abs move" style="left:257px">
    <svg width="84" height="84" viewBox="0 0 84 84"><circle cx="42" cy="42" r="30" fill="none" stroke="var(--ink)" stroke-width="3"/></svg>
    <div class="move-label">Awareness</div>
  </div>
  <div class="abs move" style="left:491px">
    <svg width="84" height="84" viewBox="0 0 84 84"><circle cx="42" cy="42" r="30" fill="none" stroke="var(--ink)" stroke-width="3"/></svg>
    <div class="move-label">Owning Your Creation</div>
  </div>
  <div class="abs move" style="left:721px">
    <svg width="84" height="84" viewBox="0 0 84 84"><circle cx="42" cy="42" r="30" fill="none" stroke="var(--ink)" stroke-width="3"/></svg>
    <div class="move-label">Reimagining</div>
  </div>
  <div class="abs move" style="left:924px">
    <svg width="84" height="84" viewBox="0 0 84 84"><circle cx="42" cy="42" r="30" fill="none" stroke="var(--ink)" stroke-width="3"/></svg>
    <div class="move-label">Manifesting</div>
  </div>
</section>

<section class="stir">
  <h2 class="abs stir-title head">Stirring the Still</h2>
  <div class="abs stir-rule"></div>
  <div class="abs stir-photo" role="img" aria-label="Speaker addressing a seated group, tinted green"></div>
  <div class="abs stir-card">
    <div class="body-text">
      <p>The Stirring the Still workshop an extension of the documentary of the same name is an <b>experiential</b> process to transform participants into disturbers of the status quo within themselves, to <b>enhance</b> their relationships with others, and to change the environments in which they exist and ultimately society for the better.</p>
      <p>This workshop experience <b>challenges</b> us all to understand the narratives we live within, to <b>look at our current roles</b> in society, and to decide what role we will play to create a more humane, just and <b>peaceful world</b>, for all. It all starts with our <b>willingness</b> to stir the ‘stillness’ of the status quo.</p>
    </div>
  </div>
</section>

<section class="community">
  <div class="abs community-bg" role="img" aria-label="Dark background of hands reaching together"></div>
  <h2 class="abs community-title head">In your community</h2>
  <p class="abs community-intro">Bring WAYmaker or the Stirring the Still workshop to your community. We would love to hear from you. Please fill out the brief form here</p>
  <div class="abs field f-name">Full Name</div>
  <div class="abs field f-mail">E-mail</div>
  <div class="abs field f-phone">Phone</div>
  <div class="abs field f-msg">Message</div>
  <div class="abs submit">SUBMIT</div>
</section>

<footer class="site-footer">
  <div class="abs footer-brand"><span class="brand-square"></span>WAYmaker</div>
  <div class="abs col col-contact">
    <div class="col-title">CONTACT US</div>
    <div class="contact-row"><svg width="10" height="14" viewBox="0 0 10 14"><path d="M5 0a5 5 0 0 0-5 5c0 4 5 9 5 9s5-5 5-9a5 5 0 0 0-5-5z" fill="var(--ink)"/><circle cx="5" cy="5" r="2" fill="#fff"/></svg><span>128 Meadow Lane<br>Fairview, ST 00000</span></div>
    <div class="contact-row"><svg width="14" height="10" viewBox="0 0 14 10"><rect width="14" height="10" fill="var(--ink)"/><path d="M1 1l6 5 6-5" stroke="#fff" fill="none"/></svg><span>hello@waymakerhub.org</span></div>
    <div class="contact-row"><svg width="12" height="12" viewBox="0 0 12 12"><path d="M2 0l3 3-1.5 2a7 7 0 0 0 3.5 3.5L9 7l3 3-2 2C5 12 0 7 0 2z" fill="var(--ink)"/></svg><span>555-014-2290</span></div>
  </div>
  <div class="abs col col-menu">
    <div class="col-title">MENU</div>
    <ul class="menu-list">
      <li>About Us</li><li>Workshops</li><li>WAYmaker Projects</li><li>Films</li><li>Store &amp; Resources</li><li>Community</li><li>Contact</li>
    </ul>
  </div>
  <div class="abs col col-connect">
    <div class="col-title">CONNECT WITH US</div>
    <div class="social-row"><span class="social-dot"></span>Circle Feed</div>
    <div class="social-row"><span class="social-dot"></span>Quick Notes</div>
    <div class="social-row"><span class="social-dot"></span>Work Network</div>
  </div>
  <div class="abs footer-rule"></div>
  <div class="abs copyright">Copyright©2018 All Rights Reserved</div>
</footer>

</body>
</html>
```